Business card for our large format printing and installation business

We want a professional looking business card for our business. We manufacture and install Signs.

On the back of the card add this info
Large Format Graphics Printing & Installations, Event Graphics, Banners, Posters, Vehicle Fleet Graphics, Boat Wraps, Wall Murals, Decals,Displays,Signs,Plaques,Digital Signs

On the Front of the card add the Tallowfern Signs logo, plus On the back of the card add the Orange Tallowfern Wraps logo. The 2 vector logos are attached to the design brief.

Target Market(s)

Local business owners

Contact Information for Business Card

Colors
f37122
f68d4e
f9ba93

Requirements
Must have
• On the Front of the card add the Tallowfern Signs logo, plus On the back of the card add the Orange Tallowfern Wraps logo. The 2 vector logos are attached to the design brief.

```html
<!DOCTYPE html>
<html lang="en">
<head>
<meta charset="utf-8">
<title>Tallowfern Signs – Business Card</title>
<link rel="stylesheet" href="https://fonts.googleapis.com/css2?family=Rubik:wght@400;500&family=Work+Sans:wght@400&display=swap">
<style>
  :root {
    --backdrop: #d8d2ca;
    --card: #efece7;
    --card-edge: #dcd6ce;
    --charcoal: #2a2624;
    --orange: #f37122;
    --orange-mid: #f68d4e;
    --orange-soft: #f9ba93;
    --ink: #2b2724;
  }
  * { margin: 0; padding: 0; box-sizing: border-box; }
  html, body {
    width: 1200px; height: 1047px; overflow: hidden;
    background: var(--backdrop);
  }
  .card {
    position: absolute; left: 100px; top: 250px;
    width: 1000px; height: 546px;
    background: var(--card);
    border: 1px solid var(--card-edge);
    border-radius: 26px;
    overflow: hidden;
    box-shadow: 0 18px 40px rgba(60, 45, 30, 0.18);
    font-family: "Work Sans", sans-serif;
    color: var(--ink);
  }
  .card__header-art {
    position: absolute; left: 0; top: 0;
    width: 1000px; height: 118px;
    background: linear-gradient(90deg, var(--orange-mid) 0%, var(--orange) 35%, var(--charcoal) 70%);
  }
  .brand-name {
    position: absolute; left: 40px; top: 152px;
    font-family: "Rubik", sans-serif; font-weight: 500;
    font-size: 46px; line-height: 1; color: var(--orange);
    display: flex; align-items: center; gap: 14px;
  }
  .brand-name__dot {
    width: 22px; height: 22px; border-radius: 50%; background: var(--orange);
  }
  .holder {
    position: absolute; right: 34px; top: 298px; text-align: right;
  }
  .holder__name {
    font-family: "Rubik", sans-serif; font-weight: 400;
    font-size: 36px; letter-spacing: 0.5px; color: var(--orange); line-height: 1;
  }
  .holder__role {
    margin-top: 12px; font-size: 21px; letter-spacing: 0.5px; color: var(--ink);
  }
  .divider {
    position: absolute; left: 38px; right: 34px; top: 380px;
    height: 2px; background: var(--orange);
  }
  .contact {
    position: absolute; left: 38px; top: 415px; list-style: none;
  }
  .contact li {
    display: flex; align-items: center; gap: 14px;
    font-size: 22px; height: 34px; letter-spacing: 0.6px;
  }
  .contact svg { width: 16px; height: 16px; flex: none; }
  .address {
    position: absolute; right: 34px; top: 449px; text-align: right;
    font-size: 22px; line-height: 34px; letter-spacing: 0.6px; font-style: normal;
  }
</style>
</head>
<body>
<section class="card">
  <div class="card__header-art" role="img" aria-label="Decorative header band in orange, yellow and charcoal tones"></div>

  <div class="brand-name"><span class="brand-name__dot"></span>Tallowfern Signs</div>

  <div class="holder">
    <div class="holder__name">DANIEL HARLOW</div>
    <div class="holder__role">Director</div>
  </div>

  <div class="divider"></div>

  <ul class="contact">
    <li>
      <svg viewBox="0 0 16 16"><path d="M3.5 1.5 L6 4.5 L4.8 6.3 C5.6 8 7.8 10.3 9.7 11.2 L11.5 10 L14.5 12.5 L12.8 14.5 C7.5 14 2 8.5 1.5 3.2 Z" fill="var(--orange)"/></svg>
      06.41.73.20.88
    </li>
    <li>
      <svg viewBox="0 0 16 16"><rect x="1.5" y="3.5" width="13" height="9" fill="none" stroke="var(--orange)" stroke-width="1.5"/><path d="M1.5 3.5 L8 9 L14.5 3.5" fill="none" stroke="var(--orange)" stroke-width="1.5"/></svg>
      info@tallowfernsigns.com
    </li>
    <li>
      <svg viewBox="0 0 16 16"><circle cx="8" cy="8" r="6.5" fill="none" stroke="var(--orange)" stroke-width="1.4"/><ellipse cx="8" cy="8" rx="2.8" ry="6.5" fill="none" stroke="var(--orange)" stroke-width="1.2"/><path d="M1.5 8 H14.5" stroke="var(--orange)" stroke-width="1.2"/></svg>
      www.tallowfernsigns.com
    </li>
  </ul>

  <address class="address">1418 Birchwood Lane<br>Marlow Falls, PA 19032</address>
</section>
</body>
</html>
```